Relocation/furniture installation company needs new business cards

we are a relocation and furniture installation company mainly dealing with corporate clients and we are looking for new business card ideas. Cards should incorporate our logo and list our website, phone number and services. The company is only 2 years old but with more staff joining we are in the need for more business cards, so something with an awesome design that is eye catching would go a long way to insure we get our name out there and look good to potential new clients.

Target Market(s)

Corporate

Industry/Entity Type

Trade

Contact Information for Business Card

www.mervoline.co.nz
0508 4 bravok

furniture installation
business relocations
joinery installation
commercial property maintenance

Colors
0592cd
34a7d8
85cae6
85acd3
0356a4
cfdfed
cee9f5
757575
474747

Requirements
Must have
• Business relocations and furniture installation specialists
Nice to have
• something that incorporates our logo.

```html
<!DOCTYPE html>
<html lang="en">
<head>
<meta charset="UTF-8">
<title>Mervoline Business Card</title>
<link href="https://fonts.googleapis.com/css2?family=Roboto:wght@400;500;700&display=swap" rel="stylesheet">
<style>
  :root {
    --page-bg: #e4e6ea;
    --card-bg: #eef0f2;
    --card-edge: #d2d6dc;
    --navy: #2c3585;
    --title-blue: #2391de;
    --text-dark: #3a3a3a;
    --icon-dark: #2f2f3a;
    --art-blue: #85acd3;
    --art-teal: #9fd6c9;
    --art-violet: #8a7fb0;
  }
  * { margin: 0; padding: 0; box-sizing: border-box; }
  html, body {
    width: 1200px;
    height: 969px;
    overflow: hidden;
    background: var(--page-bg);
    font-family: "Roboto", sans-serif;
  }
  .card {
    position: absolute;
    left: 100px;
    top: 200px;
    width: 1000px;
    height: 568px;
    background: var(--card-bg);
    border: 1px solid var(--card-edge);
    overflow: hidden;
    box-shadow: 0 10px 30px rgba(0,0,0,0.12);
  }
  .card__art {
    position: absolute;
    left: 380px;
    top: 0;
    width: 620px;
    height: 568px;
    background:
      linear-gradient(90deg, rgba(238,240,242,1) 0%, rgba(238,240,242,0) 25%),
      linear-gradient(160deg, var(--art-violet) 0%, var(--art-blue) 40%, var(--art-teal) 75%, #c7d9c8 100%);
    opacity: 0.75;
  }
  .brand {
    position: absolute;
    left: 58px;
    top: 132px;
    display: flex;
    align-items: center;
    gap: 14px;
  }
  .brand__mark {
    width: 30px;
    height: 30px;
    background: var(--navy);
  }
  .brand__name {
    font-size: 52px;
    font-weight: 500;
    letter-spacing: 4px;
    color: var(--navy);
    line-height: 1;
  }
  .person {
    position: absolute;
    left: 58px;
    top: 218px;
  }
  .person__name {
    font-size: 34px;
    font-weight: 700;
    color: var(--navy);
    line-height: 1.1;
  }
  .person__role {
    font-size: 24px;
    font-weight: 500;
    color: var(--title-blue);
    margin-top: 10px;
  }
  .details {
    position: absolute;
    left: 58px;
    top: 300px;
    list-style: none;
    font-size: 24px;
    color: var(--text-dark);
    line-height: 34px;
  }
  .details li {
    display: flex;
    align-items: flex-start;
  }
  .details__icon {
    width: 22px;
    height: 22px;
    margin: 6px 14px 0 0;
    flex: none;
  }
  .details__dot {
    width: 8px;
    height: 8px;
    border-radius: 50%;
    background: var(--icon-dark);
    margin: 13px 28px 0 7px;
    flex: none;
  }
</style>
</head>
<body>
  <div class="card">
    <div class="card__art" role="img" aria-label="Faded illustration of a modern glass office building"></div>

    <div class="brand">
      <span class="brand__mark"></span>
      <span class="brand__name">MERVOLINE</span>
    </div>

    <div class="person">
      <div class="person__name">LIAM CARTER</div>
      <div class="person__role">CEO/FOUNDER</div>
    </div>

    <ul class="details">
      <li>
        <svg class="details__icon" viewBox="0 0 24 24" aria-hidden="true">
          <path fill="#2f2f3a" d="M6.6 10.8a15.1 15.1 0 0 0 6.6 6.6l2.2-2.2a1 1 0 0 1 1-.25 11.4 11.4 0 0 0 3.6.57 1 1 0 0 1 1 1V20a1 1 0 0 1-1 1A17 17 0 0 1 3 4a1 1 0 0 1 1-1h3.5a1 1 0 0 1 1 1c0 1.25.2 2.45.57 3.57a1 1 0 0 1-.25 1z"/>
        </svg>
        0508 4 bravok
      </li>
      <li>
        <svg class="details__icon" viewBox="0 0 24 24" aria-hidden="true">
          <circle cx="12" cy="12" r="10" fill="#2f2f3a"/>
          <path d="M12 2v20M2 12h20M5 6.5c4 2 10 2 14 0M5 17.5c4-2 10-2 14 0" stroke="#eef0f2" stroke-width="1.4" fill="none"/>
        </svg>
        www.mervoline.co.nz
      </li>
      <li><span class="details__dot"></span>Furniture installation</li>
      <li><span class="details__dot"></span>Business relocations</li>
      <li><span class="details__dot"></span>Joinery installation</li>
      <li><span class="details__dot"></span>Commercial property<br>maintenance</li>
    </ul>
  </div>
</body>
</html>
```